Larkmont Business Card Design Project

Double side card , just the logo on oxford white background on one side , and the rest of the information on the other side..
the company name is : Larkmont International General Trading LLC.
logo is already attached
the card to show in the info side: company name, employee name and position (job title) phone number, fax number, email address, P.O. box, Location (city and country)
deadline is already extended 4 all to have more time... thanks

```html
<!DOCTYPE html>
<html lang="en">
<head>
<meta charset="utf-8">
<title>Larkmont Int. – Business Card</title>
<link rel="stylesheet" href="https://fonts.googleapis.com/css2?family=Open+Sans:wght@400;600;700&display=swap">
<style>
  :root {
    --backdrop: #2b2c2e;
    --card-white: #ffffff;
    --brand-blue: #1a86c8;
    --brand-cyan: #16b4e3;
    --brand-navy: #1d3f94;
    --name-blue: #1b7fc1;
    --panel-grey: #e4e5e7;
    --bar-dark: #37383c;
    --logo-grey: #55575b;
    --text-light: #ffffff;
  }
  * { margin: 0; padding: 0; box-sizing: border-box; }
  html, body {
    width: 1200px; height: 900px; overflow: hidden;
    background: var(--backdrop);
    font-family: "Open Sans", Arial, sans-serif;
  }
  .canvas { position: relative; width: 1200px; height: 900px; }
  .card {
    position: absolute; left: 230px; width: 740px; height: 410px;
    background: var(--card-white); overflow: hidden;
    box-shadow: 0 10px 30px rgba(0,0,0,.45);
  }
  .card--front { top: 30px; }
  .card--back { top: 460px; }
  .card__art { position: absolute; inset: 0; width: 100%; height: 100%; }

  .wordmark {
    position: absolute; display: flex; align-items: center; gap: 14px;
    font-weight: 600; letter-spacing: 3px; color: var(--logo-grey);
    text-transform: uppercase; white-space: nowrap;
  }
  .wordmark__dot { border-radius: 50%; background: var(--brand-blue); }
  .card--front .wordmark { left: 190px; top: 178px; font-size: 44px; }
  .card--front .wordmark__dot { width: 30px; height: 30px; }
  .card--back .wordmark { left: 70px; top: 120px; font-size: 36px; }
  .card--back .wordmark__dot { width: 24px; height: 24px; }

  .holder { position: absolute; right: 36px; top: 212px; text-align: right; }
  .holder__name { font-size: 23px; font-weight: 700; color: var(--name-blue); letter-spacing: 1px; text-transform: uppercase; line-height: 1.1; }
  .holder__role { font-size: 20px; font-weight: 400; color: var(--name-blue); line-height: 1.1; }

  .address {
    position: absolute; left: 26px; top: 262px;
    font-size: 19px; color: var(--text-light); white-space: nowrap;
  }
  .contact {
    position: absolute; top: 318px; display: flex; align-items: center; gap: 16px;
    color: var(--text-light); font-size: 18px; line-height: 1.45;
  }
  .contact--phone { left: 48px; }
  .contact--online { left: 350px; }
  .contact__icon { width: 34px; height: 34px; flex: none; }
</style>
</head>
<body>
<main class="canvas">

  <section class="card card--front" aria-label="Business card, logo side">
    <svg class="card__art" viewBox="0 0 740 410" aria-hidden="true">
      <defs>
        <linearGradient id="frontBand" x1="0" y1="0" x2="1" y2="0">
          <stop offset="0" stop-color="#16b4e3"/>
          <stop offset="1" stop-color="#1d3f94"/>
        </linearGradient>
        <linearGradient id="frontWedge" x1="1" y1="0" x2="0" y2="0">
          <stop offset="0" stop-color="#1d3f94"/>
          <stop offset="1" stop-color="#16b4e3"/>
        </linearGradient>
      </defs>
      <polygon points="0,0 740,0 740,50 0,78" fill="url(#frontBand)"/>
      <polygon points="740,215 740,270 330,332" fill="url(#frontWedge)"/>
    </svg>
    <div class="wordmark"><span class="wordmark__dot"></span>Larkmont Int.</div>
  </section>

  <section class="card card--back" aria-label="Business card, contact side">
    <svg class="card__art" viewBox="0 0 740 410" aria-hidden="true">
      <polygon points="470,190 740,190 740,300 430,300" fill="var(--panel-grey)"/>
      <polygon points="0,252 462,252 440,300 0,300" fill="var(--brand-blue)"/>
      <rect x="0" y="300" width="740" height="110" fill="var(--bar-dark)"/>
    </svg>

    <div class="wordmark"><span class="wordmark__dot"></span>Larkmont Int.</div>

    <div class="holder">
      <p class="holder__name">Dara K. Whitfield</p>
      <p class="holder__role">CEO</p>
    </div>

    <p class="address">214 Fernhill Lane, Ashford, MO 64720</p>

    <div class="contact contact--phone">
      <svg class="contact__icon" viewBox="0 0 34 34" aria-hidden="true">
        <circle cx="17" cy="17" r="15" fill="none" stroke="#fff" stroke-width="2"/>
        <path d="M11 10 l4 0 l1 5 l-2 1.5 a10 10 0 0 0 5 5 l1.5 -2 l5 1 l0 4 a2 2 0 0 1 -2 2 a16 16 0 0 1 -14.5 -14.5 a2 2 0 0 1 2 -2z" fill="#fff"/>
      </svg>
      <div>
        <p>+ 555-010-4821</p>
        <p>+ 555-010-4822(F)</p>
      </div>
    </div>

    <div class="contact contact--online">
      <svg class="contact__icon" viewBox="0 0 34 34" aria-hidden="true">
        <text x="17" y="27" text-anchor="middle" font-size="30" font-family="Open Sans, Arial, sans-serif" fill="#fff">@</text>
      </svg>
      <div>
        <p>DaraKWhitfield@hollowmere.com</p>
        <p>www.hollowmere.com</p>
      </div>
    </div>
  </section>

</main>
</body>
</html>
```